Brightwell Settlement Brochure/Flyer Revisions

Improve the current design and over all look for Tri-Fold brochure and 8 x 11 flyer along with update the text and view picture substitutions.

Target Market(s)

Currently our brochure is geared more towards the Cancer Patient, and less Senior.
I want to take the new revisions text, or new message, and incorporate it into the new designed brochure and flyer. I want a nice picture of a senior or couple to be primary view shot and the cancer patients secondary.
Please visit our website; www.brightwellsettlements.org

Requirements
Must have
• we want all Seniors and Cancer Patients that own a life insurance policy, group or individual to call us. We want the consumer to be educated and know their rights.
Brightwell Settlements will be there ADVOCATE and Financial RESOURCE

```html
<!DOCTYPE html>
<html lang="en">
<head>
<meta charset="utf-8">
<title>Brightwell Settlements Tri-Fold Brochure</title>
<link href="https://fonts.googleapis.com/css2?family=Questrial&family=Poppins:wght@500;600;700&display=swap" rel="stylesheet">
<style>
  :root {
    --page-bg: #f0f0f0;
    --magenta: #a43f8f;
    --magenta-deep: #8e3279;
    --brown: #5a3a2c;
    --teal: #1f6a78;
    --blue-deep: #2c5a9a;
    --green: #3f6b2e;
    --white: #ffffff;
    --strip: #e9e4df;
    --brand-blue: #1f63b8;
    --ink-grey: #8a8a8a;
  }
  * { box-sizing: border-box; margin: 0; padding: 0; }
  html, body { width: 1200px; height: 1000px; overflow: hidden; background: var(--page-bg); }
  body { font-family: "Questrial", "Century Gothic", sans-serif; color: var(--white); }

  .brochure {
    position: absolute; left: 120px; top: 150px;
    width: 960px; height: 700px;
    display: flex;
    box-shadow: 0 6px 22px rgba(0,0,0,.18);
  }
  .panel { position: relative; width: 320px; height: 100%; overflow: hidden; }

  /* Left panel */
  .panel--cover .photo {
    position: absolute; inset: 0;
    background: linear-gradient(160deg, #3f6b2e 0%, #6f8f4a 35%, #c9a894 55%, #8d98a8 80%, #b9c2cc 100%);
  }
  .discover {
    position: absolute; left: 0; bottom: 38px; width: 312px;
  }
  .discover__tab {
    background: var(--white); height: 40px; width: 296px;
    padding: 2px 0 0 20px;
    font-family: "Poppins", sans-serif; font-weight: 600;
    font-size: 30px; color: var(--magenta); line-height: 38px;
  }
  .discover__body {
    background: var(--magenta); padding: 12px 16px 16px 20px;
    font-size: 14px; line-height: 1.2; text-align: justify;
  }
  .discover__body p + p { margin-top: 0; }
  .discover__body .gap { margin-top: 17px; }

  /* Middle panel */
  .panel--call {
    background: linear-gradient(180deg, #1e5d3a 0%, #1f6a78 35%, #2b5c9c 70%, #35508f 92%);
  }
  .questions { font-size: 14.5px; line-height: 1.1; text-align: justify; }
  .questions p { margin: 0; }
  .panel--call .questions--top { position: absolute; left: 22px; right: 16px; top: 230px; }
  .panel--call .questions--bottom { position: absolute; left: 22px; right: 16px; top: 435px; }
  .call {
    position: absolute; left: 20px; right: 12px; top: 330px;
  }
  .call__label {
    font-size: 13.5px; letter-spacing: 2px; margin: 18px 0 0 6px;
  }
  .call__brand {
    position: absolute; right: 0; top: 0; width: 105px; height: 56px;
    background: var(--white); border-radius: 10px 10px 0 10px;
    display: flex; align-items: center; gap: 5px; padding: 0 7px;
    color: var(--brand-blue); font-size: 11px; line-height: 1.1;
  }
  .call__brand .dot { width: 10px; height: 10px; border-radius: 50%; background: var(--brand-blue); flex: none; }
  .call__phone {
    margin-top: 16px; background: var(--white); border-radius: 14px;
    height: 36px; text-align: center;
    font-size: 27px; letter-spacing: 2px; color: var(--blue-deep); line-height: 36px;
  }
  .strip {
    position: absolute; left: 0; right: 0; bottom: 0; height: 40px;
    background: var(--strip);
    display: flex; align-items: center;
  }
  .contact { justify-content: flex-end; padding-right: 20px; gap: 6px; color: var(--blue-deep); font-size: 18px; }
  .contact__label { margin-right: 6px; font-family: Arial, sans-serif; }
  .contact .square { width: 22px; height: 22px; background: var(--blue-deep); border-radius: 3px; }

  /* Right panel */
  .panel--healing {
    background: linear-gradient(180deg, #4e3327 0%, #6a3c3a 30%, #9a3f83 42%, var(--magenta) 60%, var(--magenta-deep) 100%);
  }
  .healing-photo {
    position: absolute; left: 50%; top: 105px; transform: translateX(-50%);
    width: 168px; height: 168px; border-radius: 50%;
    background: #d9d9de; padding: 10px;
    box-shadow: 0 4px 12px rgba(0,0,0,.35);
  }
  .healing-photo .photo {
    width: 100%; height: 100%; border-radius: 50%;
    background: radial-gradient(circle at 50% 45%, #e4b99a 0%, #a7b7cf 45%, #2f5aa8 100%);
  }
  .headline { position: absolute; left: 0; right: 0; top: 322px; text-align: center; }
  .headline__main {
    font-family: "Poppins", sans-serif; font-weight: 600; font-size: 24px; line-height: 1.1; letter-spacing: .3px;
  }
  .headline__sub { font-size: 12.5px; }
  .headline__accent {
    font-family: "Poppins", sans-serif; font-weight: 700; font-size: 34px; line-height: 1.2;
  }
  .panel--healing .questions { position: absolute; left: 18px; right: 18px; top: 440px; }
  .web { padding-left: 16px; color: var(--magenta); font-size: 14px; letter-spacing: 3.5px; font-style: italic; }
</style>
</head>
<body>
  <main class="brochure">
    <section class="panel panel--cover">
      <div class="photo" role="img" aria-label="Photograph of a cancer patient gazing thoughtfully outdoors against green foliage"></div>
      <div class="discover">
        <h2 class="discover__tab">Discover</h2>
        <div class="discover__body">
          <p>Why do insurance companies conceal the fact that policy holders may be entitled to additional cash benefits?</p>
          <p>Why are bankruptcy rates among cancer patients and seniors more than double than that of the general population?</p>
          <p class="gap">Why do patients without financial stress</p>
        </div>
      </div>
    </section>

    <section class="panel panel--call">
      <div class="questions questions--top">
        <p>Why do insurance companies conceal the fact that policy holders may be entitled to additional cash benefits?</p>
        <p>Why are bankruptcy rates among cancer patients and seniors more than double than</p>
      </div>
      <div class="call">
        <div class="call__brand"><span class="dot"></span><span>Brightwell Settlements</span></div>
        <p class="call__label">Give Us a call with</p>
        <p class="call__phone">800-<strong>555</strong>-0142</p>
      </div>
      <div class="questions questions--bottom">
        <p>Why do insurance companies conceal the fact that policy holders may be entitled to additional cash benefits?</p>
        <p>Why are bankruptcy rates among cancer patients and seniors more than double than that of the general population?</p>
        <p>Why do patients without financial stress have significantly faster improvement rates over time in functional, emotional, and physical well-being as compared with patients who faced economic burdens?</p>
      </div>
      <div class="strip contact">
        <span class="contact__label">Contact us via:</span>
        <span class="square"></span><span class="square"></span><span class="square"></span>
      </div>
    </section>

    <section class="panel panel--healing">
      <div class="healing-photo"><div class="photo" role="img" aria-label="Photograph of a caregiver holding an elderly patient's hands"></div></div>
      <div class="headline">
        <h2 class="headline__main">HEALING &amp; RECOVERY</h2>
        <p class="headline__sub">should be the primary concern of patients</p>
        <p class="headline__accent">“NOT MONEY”</p>
      </div>
      <div class="questions">
        <p>Why do insurance companies conceal the fact that policy holders may be entitled to additional cash benefits?</p>
        <p>Why are bankruptcy rates among cancer patients and seniors more than double than that of the general population?</p>
        <p>Why do patients without financial stress have significantly faster improvement rates over time in functional, emotional, and physical well-being as compared with patients who faced economic burdens?</p>
      </div>
      <div class="strip"><span class="web">www.brightwellsettlements.org</span></div>
    </section>
  </main>
</body>
</html>
```